Cover Page for Financial Statements

We need a cover page designed for our Financial Statements. It will need to include our business logo and the Chartered accountant logo.
We have included our current title page ( image titled full.png ) to show all the information that is needed to be included such as the title 'Financial Statements' and 'The year ended March 2023'. We would like to see designs that reflect our logo but also adds some interest with objects / deisngs that fill up more of the page.

Industry/Entity Type

Accounting

Font styles to use
Serif
Sans Serif

Colors

Designer to choose only greyscale colors for use in the design.

Requirements
Must have
• - A4 document size, our logo, Chartered Accountant Logo
Should not have
• Bright Colors

```html
<!DOCTYPE html>
<html lang="en">
<head>
<meta charset="utf-8">
<title>Financial Statement Cover – 31 March 2023</title>
<link rel="stylesheet" href="https://fonts.googleapis.com/css2?family=Oswald:wght@400;500;600&family=Montserrat:wght@500;600&display=swap">
<style>
  :root {
    --backdrop: #e4e4e4;
    --paper: #ffffff;
    --ink: #2f2f2f;
    --grey-900: #262626;
    --grey-800: #3c3c3c;
    --grey-700: #555555;
    --grey-600: #6e6e6e;
    --grey-500: #878787;
    --grey-400: #a3a3a3;
    --grey-300: #bdbdbd;
    --grey-200: #d6d6d6;
    --mark-fill: #5e5e5e;
  }
  * { box-sizing: border-box; margin: 0; padding: 0; }
  html, body {
    width: 975px;
    height: 1200px;
    overflow: hidden;
    background: var(--backdrop);
  }
  .cover {
    position: absolute;
    left: 63px;
    top: 0;
    width: 848px;
    height: 1200px;
    background: var(--paper);
    overflow: hidden;
    font-family: "Montserrat", sans-serif;
  }
  .cover__art {
    position: absolute;
    inset: 0;
    width: 848px;
    height: 1200px;
  }
  .institute {
    position: absolute;
    left: 64px;
    top: 50px;
    width: 236px;
    text-align: center;
    color: var(--ink);
    font-family: "Montserrat", sans-serif;
    font-weight: 600;
  }
  .institute__dot {
    display: block;
    width: 90px;
    height: 90px;
    margin: 0 auto 20px;
    border-radius: 50%;
    background: var(--mark-fill);
  }
  .institute__name {
    display: block;
    font-size: 13.5px;
    letter-spacing: 1.2px;
    line-height: 1;
  }
  .institute__region {
    display: block;
    margin-top: 6px;
    font-size: 9.5px;
    letter-spacing: 0.9px;
    line-height: 1;
  }
  .title {
    position: absolute;
    left: 95px;
    top: 950px;
    width: 400px;
    font-family: "Oswald", sans-serif;
    font-weight: 400;
    line-height: 1;
  }
  .title__main {
    display: block;
    white-space: nowrap;
    font-size: 54px;
    font-weight: 600;
    letter-spacing: -1px;
    text-transform: uppercase;
    transform: scaleX(0.85);
    transform-origin: left center;
  }
  .title__main span {
    -webkit-background-clip: text;
    background-clip: text;
    color: transparent;
  }
  .title__word--first {
    background-image: linear-gradient(90deg, var(--grey-900), var(--grey-700));
  }
  .title__word--second {
    background-image: linear-gradient(90deg, var(--grey-600), var(--grey-400));
  }
  .title__period {
    display: block;
    white-space: nowrap;
    margin-top: 0;
    font-size: 53px;
    font-weight: 400;
    letter-spacing: -1.5px;
    color: var(--ink);
    text-transform: uppercase;
    transform: scaleX(0.84);
    transform-origin: left center;
  }
  .title__date {
    display: inline-block;
    white-space: nowrap;
    margin-top: 6px;
    font-size: 33px;
    font-weight: 600;
    letter-spacing: 8px;
    background-image: linear-gradient(90deg, var(--grey-900), var(--grey-700) 40%, var(--grey-500) 70%, var(--grey-400));
    -webkit-background-clip: text;
    background-clip: text;
    color: transparent;
  }
  .firm {
    position: absolute;
    left: 560px;
    top: 1046px;
    width: 205px;
    color: var(--ink);
    font-family: "Montserrat", sans-serif;
    font-weight: 500;
    line-height: 1;
  }
  .firm__name {
    display: block;
    font-size: 21px;
    letter-spacing: 1.5px;
  }
  .firm__tagline {
    display: block;
    margin-top: 8px;
    font-size: 7.5px;
    letter-spacing: 1.6px;
    text-align: right;
  }
</style>
</head>
<body>
  <main class="cover">
    <svg class="cover__art" viewBox="0 0 848 1200" xmlns="http://www.w3.org/2000/svg">
      <defs>
        <linearGradient id="crescentGrad" x1="0" y1="0" x2="0" y2="1">
          <stop offset="0" stop-color="#b5b5b5"/>
          <stop offset="1" stop-color="#7d7d7d"/>
        </linearGradient>
        <linearGradient id="upperBandGrad" x1="0" y1="0" x2="1" y2="0">
          <stop offset="0" stop-color="#d4d4d4"/>
          <stop offset="0.45" stop-color="#a8a8a8"/>
          <stop offset="0.62" stop-color="#7a7a7a"/>
          <stop offset="1" stop-color="#3e3e3e"/>
        </linearGradient>
        <linearGradient id="lowerBandGrad" x1="0" y1="0" x2="1" y2="0">
          <stop offset="0" stop-color="#808080"/>
          <stop offset="0.5" stop-color="#a6a6a6"/>
          <stop offset="1" stop-color="#d2d2d2"/>
        </linearGradient>
        <linearGradient id="baseBandGrad" x1="0" y1="0" x2="1" y2="0">
          <stop offset="0" stop-color="#8a8a8a"/>
          <stop offset="0.5" stop-color="#b0b0b0"/>
          <stop offset="0.7" stop-color="#6c6c6c"/>
          <stop offset="1" stop-color="#454545"/>
        </linearGradient>
        <linearGradient id="ringGrad" x1="0" y1="0" x2="1" y2="1">
          <stop offset="0" stop-color="#3a3a3a"/>
          <stop offset="0.5" stop-color="#7c7c7c"/>
          <stop offset="1" stop-color="#b8b8b8"/>
        </linearGradient>
        <linearGradient id="cityGrad" x1="0" y1="0" x2="0" y2="1">
          <stop offset="0" stop-color="#b2b2b2"/>
          <stop offset="0.3" stop-color="#7e7e7e"/>
          <stop offset="0.45" stop-color="#686868"/>
          <stop offset="0.7" stop-color="#4a4a4a"/>
          <stop offset="1" stop-color="#929292"/>
        </linearGradient>
        <radialGradient id="tabletGrad" cx="0.5" cy="0.55" r="0.6">
          <stop offset="0" stop-color="#b8b8b8"/>
          <stop offset="0.6" stop-color="#707070"/>
          <stop offset="1" stop-color="#2e2e2e"/>
        </radialGradient>
      </defs>

      <path class="swoosh swoosh--crescent" d="M541,88 C380,140 222,300 222,514 L304,517 C300,330 400,170 541,88 Z" fill="url(#crescentGrad)"/>
      <path class="swoosh swoosh--upper" d="M298,422 C310,250 460,93 640,93 C740,93 810,125 848,156 L848,254 C790,210 710,184 620,184 C470,184 340,280 298,422 Z" fill="url(#upperBandGrad)"/>
      <path class="swoosh swoosh--lower" d="M406,684 C470,716 550,728 630,726 C730,722 800,680 848,640 L848,694 C790,750 720,776 630,776 C540,776 460,756 398,726 Z" fill="url(#lowerBandGrad)"/>
      <path class="swoosh swoosh--base" d="M366,786 L403,756 C470,784 540,794 620,794 C720,794 800,760 848,711 L848,803 C790,850 710,878 620,878 C520,878 430,840 366,786 Z" fill="url(#baseBandGrad)"/>

      <ellipse class="photo photo--city" cx="584" cy="468" rx="266" ry="253" fill="url(#cityGrad)" role="img" aria-label="Aerial photograph of a city skyline beside a river"/>

      <circle class="frame__ring" cx="263" cy="670" r="144" fill="url(#ringGrad)"/>
      <circle class="frame__gap" cx="263" cy="670" r="131" fill="#ffffff"/>
      <circle class="photo photo--tablet" cx="263" cy="670" r="117" fill="url(#tabletGrad)" role="img" aria-label="Photograph of a hand holding a tablet with business charts and icons"/>
    </svg>

    <div class="institute">
      <span class="institute__dot"></span>
      <span class="institute__name">LEDGER PROFESSIONALS</span>
      <span class="institute__region">PACIFIC REGION</span>
    </div>

    <h1 class="title">
      <span class="title__main"><span class="title__word--first">Financial</span> <span class="title__word--second">Statement</span></span>
      <span class="title__period">For the year ended</span>
      <span class="title__date">31 MARCH 2023</span>
    </h1>

    <div class="firm">
      <span class="firm__name">SUMMIT LEDGER</span>
      <span class="firm__tagline">ACCOUNTING &amp; ADVISORY</span>
    </div>
  </main>
</body>
</html>
```